Letterhead for a German Distribution/Manufacturing Company

We need a professional Letterhead in a unique Design.
not to playful.
The Letterhead has to show show that we are a international company with headquater in Germany.
all details like adress, Vat Tax Number, Bank Accout, Eori, email, Company number has to be on the Letterhead.
for example use: VAT TAX DE5140683 Bank Account: Halmer Kreditbank IBAN DE417052381ß240316 Swift: HKRB0513742 EORI 3150827469 Company Number: HRB 58106 Adress: VOLINTRA UG Tannwiesen Strasse 7 Postal Code 09385 City Weilborn Country: Germany Email: info@volintra-mail.net
the design can be colored but doesnt have to be
Industry/Entity Type
Manufacturing and international distribution
Requirements
Must have
- show that we are a international company with headquater in Germany. our company infos and logo

```html
<!DOCTYPE html>
<html lang="en">
<head>
<meta charset="utf-8">
<title>VOLINTRA Letterhead</title>
<link rel="stylesheet" href="https://fonts.googleapis.com/css2?family=Lato:wght@400;700&family=Montserrat:wght@500;600&family=Parisienne&display=swap">
<style>
  :root {
    --canvas-bg: #e6e6e6;
    --paper: #ffffff;
    --ink: #1f1f1f;
    --ink-soft: #333333;
    --brand: #3b3b3b;
    --rule: #2a2a2a;
  }
  * { margin: 0; padding: 0; box-sizing: border-box; }
  html, body { width: 1200px; height: 1200px; overflow: hidden; }
  body { background: var(--canvas-bg); position: relative; }

  .letterhead {
    position: absolute;
    left: 204px; top: 40px;
    width: 792px; height: 1120px;
    background: var(--paper);
    box-shadow: 0 4px 18px rgba(0,0,0,0.18);
    color: var(--ink);
    font-family: "Lato", sans-serif;
  }

  .brand {
    position: absolute;
    top: 56px; left: 0; width: 100%;
    display: flex; justify-content: center; align-items: center; gap: 14px;
  }
  .brand-dot { width: 38px; height: 38px; border-radius: 50%; background: var(--brand); }
  .brand-name {
    font-family: "Lato", sans-serif;
    font-weight: 400;
    font-size: 44px;
    letter-spacing: 1px;
    color: var(--brand);
    line-height: 1;
  }

  .company-details {
    position: absolute;
    top: 116px; left: 0; width: 100%;
    text-align: center;
    font-family: "Montserrat", sans-serif;
    font-weight: 600;
    font-size: 12px;
    line-height: 19.5px;
    color: var(--ink);
  }
  .header-rule {
    position: absolute;
    top: 240px; left: 300px;
    width: 192px; height: 2px;
    background: var(--rule);
  }

  .letter { position: absolute; left: 46px; right: 46px; top: 343px; }
  .letter p, .letter address { font-size: 15px; line-height: 19px; color: var(--ink-soft); font-style: normal; }
  .date { margin-bottom: 20px; }
  .recipient-name { margin-bottom: 19px; }
  .salutation { font-size: 18px !important; font-weight: 700; margin: 24px 0 20px; color: var(--ink) !important; }
  .body-copy p { text-align: justify; font-weight: 700; font-size: 14.8px; margin-bottom: 17px; line-height: 18.2px; }
  .closing { font-size: 13px !important; font-weight: 700; margin-top: 40px; }
  .signature {
    font-family: "Parisienne", cursive;
    font-size: 38px !important;
    line-height: 1.2 !important;
    color: var(--ink) !important;
    margin-top: 30px;
  }
</style>
</head>
<body>
  <article class="letterhead">
    <header>
      <div class="brand">
        <span class="brand-dot"></span>
        <span class="brand-name">VOLINTRA</span>
      </div>
      <div class="company-details">
        VAT TAX DE5140683<br>
        Bank Account: Halmer Kreditbank IBAN DE417052381ß240316 Swift: HKRB0513742<br>
        EORI 3150827469<br>
        Company Number: HRB 58106<br>
        Adress: VOLINTRA UG Tannwiesen Strasse 7 Postal Code 09385 City Weilborn Country<br>
        Germany Email: info@volintra-mail.net
      </div>
      <div class="header-rule"></div>
    </header>

    <section class="letter">
      <p class="date">January-03-2020</p>
      <address class="recipient-name">Mr, Jonas Brandt<br>President</address>
      <address class="recipient-company">Norvale Corporation<br>123 Street Name, Suite# 10<br>City, State, 120023</address>
      <p class="salutation">Dear Mr, Jonas</p>
      <div class="body-copy">
        <p>Lorem ipsum dolor sit amet, consectetur adipisicing elit, sed do eiusmod tempor incididunt ut labore et dolore magna aliqua. Ut enim ad minim veniam, quis nostrud exercitation ullamco laboris nisi ut aliquip ex ea commodo consequat. Duis aute irure dolor in reprehenderit in voluptate velit esse cillum dolore eu fugiat nulla pariatur.</p>
        <p>Lorem ipsum dolor sit amet, consectetur adipisicing elit, sed do eiusmod tempor incididunt ut labore et dolore magna aliqua. Ut enim ad minim veniam, quis nostrud exercitation ullamco laboris nisi ut aliquip ex ea commodo consequat. Duis aute irure dolor in reprehenderit in voluptate velit esse cillum dolore eu fugiat nulla pariatur.</p>
        <p>Lorem ipsum dolor sit amet, consectetur adipisicing elit, sed do eiusmod tempor incididunt ut labore et dolore magna aliqua. Ut enim ad minim veniam, quis nostrud exercitation ullamco laboris nisi ut aliquip ex ea commodo consequat.</p>
        <p>Excepteur sint occaecat cupidatat non proident, sunt in culpa qui officia deserunt mollit anim id est laborum. re et dolore magnam aliquam quaerat voluptatem.</p>
      </div>
      <p class="closing">Regards</p>
      <p class="signature">Martin Keller</p>
    </section>
  </article>
</body>
</html>
```